Climb Onward 2015

We're repeating the same promo in 2015 as a promo called Climb Onward for 2014. We simply need the look of the flyer changed for 2015. The concept is: we're better than the competition and we want to prove it. (without saying that) :)

Target Market(s)

This flyer will go to roofing contractors that do not use our company for their roofing needs. We would like them to try us and for that they get $500 off their order after buying $10K worth. We want an opportunity to prove to them that they will prefer us!

Industry/Entity Type

Promo

Colors
0356a4

Requirements
Must have
• Must not directly mention "competition"
Must be fairly reserved and male oriented (roofing contractors)
Title must be "Climb Onward in 2015"
Must have our logo & website www.harborfinchdepot.example
Must have Terms and Conditions (with Expiration of Dec 31, 2016)
Nice to have
• A design that POPS!
Feel free to add things that you think will work
Be creative

```html
<!DOCTYPE html>
<html lang="en">
<head>
<meta charset="utf-8">
<title>Climb Onward in 2015 – Harborfinch Depot</title>
<link href="https://fonts.googleapis.com/css2?family=Questrial&family=Arimo:wght@400;700&display=swap" rel="stylesheet">
<style>
  :root {
    --backdrop: #b9c6c6;
    --paper: #ffffff;
    --ink: #1a1a1a;
    --brand-blue: #0356a4;
    --band-dark: #151515;
    --band-grey-top: #f2f2f2;
    --band-grey-bottom: #c9c9c9;
    --accent: #f15a22;
    --text-light: #ffffff;
    --photo-light: #f4f4f4;
    --photo-mid: #d4d4d4;
    --photo-dark: #4a4a4a;
  }
  * { box-sizing: border-box; margin: 0; padding: 0; }
  html, body { width: 1200px; height: 638px; overflow: hidden; }
  body {
    background: var(--backdrop);
    font-family: "Arimo", Arial, sans-serif;
    color: var(--ink);
    position: relative;
  }
  .flyer {
    position: absolute;
    left: 350px;
    top: 14px;
    width: 500px;
    height: 610px;
    background: var(--paper);
    display: flex;
    flex-direction: column;
    box-shadow: 0 4px 14px rgba(0,0,0,0.25);
    overflow: hidden;
  }
  .team-photo {
    position: relative;
    height: 222px;
    flex: none;
    background:
      radial-gradient(ellipse 48% 70% at 66% 62%, rgba(74,74,74,0.85) 0%, rgba(74,74,74,0.35) 50%, rgba(212,212,212,0) 80%),
      linear-gradient(90deg, var(--photo-light) 0%, var(--photo-light) 25%, var(--photo-mid) 100%);
  }
  .brand {
    position: absolute;
    left: 18px;
    top: 16px;
    display: flex;
    align-items: center;
    gap: 7px;
    font-family: "Questrial", "Century Gothic", sans-serif;
    font-size: 16px;
    color: var(--brand-blue);
  }
  .brand-mark {
    width: 14px;
    height: 14px;
    background: var(--brand-blue);
  }
  .title-band {
    height: 46px;
    flex: none;
    background: linear-gradient(180deg, var(--band-grey-top), var(--band-grey-bottom));
    display: flex;
    align-items: center;
    justify-content: center;
  }
  .title-band h1 {
    font-family: "Questrial", "Century Gothic", sans-serif;
    font-weight: 400;
    font-size: 31px;
    letter-spacing: -0.3px;
  }
  .voucher-band {
    height: 50px;
    flex: none;
    background: var(--band-dark);
    color: var(--text-light);
    display: flex;
    align-items: center;
    justify-content: center;
  }
  .voucher-band h2 {
    font-family: "Questrial", "Century Gothic", sans-serif;
    font-weight: 400;
    font-size: 30px;
  }
  .voucher-band .amount { color: var(--accent); }
  .confidence {
    height: 46px;
    flex: none;
    display: flex;
    align-items: center;
    justify-content: center;
    text-align: center;
    font-weight: 700;
    font-size: 13px;
    line-height: 1.3;
    padding: 0 40px;
  }
  .difference {
    height: 122px;
    flex: none;
    background: var(--band-dark);
    color: var(--text-light);
    padding: 7px 20px 0 22px;
  }
  .difference h3 {
    font-family: "Questrial", "Century Gothic", sans-serif;
    font-weight: 400;
    font-size: 22px;
    line-height: 1;
    margin-bottom: 5px;
  }
  .difference ul { list-style: none; font-size: 9px; line-height: 1.25; }
  .difference li::before { content: "- "; }
  .offer-details {
    height: 58px;
    flex: none;
    display: flex;
    align-items: center;
    justify-content: center;
    text-align: center;
    font-size: 12px;
    line-height: 1.3;
    padding: 0 38px;
  }
  .terms {
    flex: 1;
    background: var(--accent);
    color: var(--text-light);
    font-size: 7px;
    line-height: 1.45;
    padding: 9px 22px;
  }
  .terms .website { font-weight: 700; }
</style>
</head>
<body>
  <main class="flyer">
    <div class="team-photo" role="img" aria-label="Photo of a confident team of four business professionals in suits">
      <div class="brand"><span class="brand-mark"></span>Harborfinch Depot</div>
    </div>
    <div class="title-band"><h1>Climb Onward in 2015</h1></div>
    <div class="voucher-band"><h2>Receive a <span class="amount">$500.00</span> Voucher</h2></div>
    <p class="confidence">After 40 Years of Servicing the Professional Contractor and Home Builder, We are Confident We Can Win You Over!</p>
    <section class="difference">
      <h3>Discover the Harborfinch Difference</h3>
      <ul>
        <li>Triple Check System for Accurate Delivery</li>
        <li>Inventory of Major Brands</li>
        <li>Take Off Services</li>
        <li>New Fleet Monitored by Trackwell</li>
        <li>Finance Options</li>
        <li>Marketing Programs to Increase Your Job Leads</li>
        <li>Online Bill Pay</li>
      </ul>
    </section>
    <p class="offer-details">New customers who have purchased less than $2,000 in the past 6 months will be issued a $500 voucher, upon purchasing $10,000, to be used for additional purchases at Harborfinch Depot. One voucher per customer.</p>
    <p class="terms">Terms and Conditions: Voucher is issued for future purchases only and may not be applied to any prior balance or current invoice. Cannot be combined with other offers. Void where prohibited. Harborfinch Depot may change or end this offer at any time without notice. Expires December 31, 2016. All rights reserved. <span class="website">www.harborfinchdepot.example</span></p>
  </main>
</body>
</html>
```